Package Storage Service

Ideas...

Business Name... "TUCK IT AT BRAMWOOD":
Store it,
Don’t Ship it;
4-LESS
Convenience, Quality, Service

Easy as ABC…
A. Contact Us 064-293-5527
B. We deliver
C. We pick-up & Store

LESS, is the new MORE

Box Size* (Approx) Weight Limit Price per Month
41 cm X 34 cm X 26 cm 10 Kilos 12 CHFs/per month
48 cm X 43 cm X 35 cm 25 Kilos 25 CHFs/per month

* Larger sizes and prices available upon request.

Contact: Tom /064-293-5527

These are only ideas for a small package storage service for local college students. The storage times are usually for 1 - 3 months.
I need a catchy, creative, colorful design for a new business.

This flyer will need to be printable in color. A-4 size or 8 1/2 " X 11".

Target Market(s)

Hotel Management students leaving their program for vacations for short terms. They return after vacation or after practical work experiences 4 study.

Industry/Entity Type

College

Requirements
Must have
• Prices, box sizes, catchy format.

Idea will forward to their address should they not return to the school; for a postage fee + 15.00 CHFs.

Contact information for the PICKUP and DELIVERY Service... see above.

Include a PICKUP AND DELIVERY Option in the flyer.
Nice to have
• Colorful boxes with a creative idea for someone to choose spending a little each month rather than a lot at one time. 25 CHFs rather than 125 CHFs.
Should not have
• Not too wordy.

```html
<!DOCTYPE html>
<html lang="en">
<head>
<meta charset="utf-8">
<title>Tuck It At Bramwood – Package Storage</title>
<link rel="stylesheet" href="https://fonts.googleapis.com/css2?family=Archivo+Black&family=Arimo:wght@400;700&display=swap">
<style>
  :root {
    --orange: #f24e0e;
    --dark: #2b201b;
    --yellow: #fff200;
    --white: #ffffff;
    --kraft-light: #e2c48c;
    --kraft-dark: #b88f52;
    --muted: #c9bdb5;
  }
  html, body { margin: 0; padding: 0; overflow: hidden; }
  body { width: 849px; height: 1200px; }
  .flyer {
    position: relative;
    width: 849px;
    height: 1200px;
    background: var(--orange);
    overflow: hidden;
    font-family: "Arimo", Arial, sans-serif;
  }
  .top-band { position: absolute; left: 0; top: 0; width: 100%; height: 11px; background: var(--dark); }

  .headline { position: absolute; left: 0; width: 100%; margin: 0; text-align: center;
    font-family: "Archivo Black", "Arial Black", sans-serif; line-height: 1; }
  .business-name { top: 40px; font-size: 58px; color: var(--white); letter-spacing: 0.5px; }
  .tagline { top: 112px; font-size: 52px; color: var(--yellow); }
  .benefit { font-size: 68px; color: var(--white);
    -webkit-text-stroke: 2px var(--dark);
    text-shadow: 3px 3px 0 var(--dark); }
  .benefit-less { top: 168px; }
  .benefit-convenience { top: 230px; }
  .benefit-quality { top: 292px; }
  .benefit-service { top: 354px; }

  .box-illustration { position: absolute; left: 164px; top: 420px; width: 506px; height: 578px;
    background: radial-gradient(ellipse at 50% 45%, var(--kraft-light), var(--kraft-dark));
    border-radius: 6px; }

  .price-table { position: absolute; left: 427px; top: 1014px; width: 382px;
    border-collapse: collapse; font-size: 12.5px; color: var(--white); }
  .price-table th { background: var(--dark); font-weight: 700; text-align: left; padding: 2px 5px; }
  .price-table td { border: 1px solid var(--dark); padding: 2px 5px; white-space: nowrap; }
  .footnote { position: absolute; left: 427px; top: 1072px; margin: 0; font-size: 9px; color: var(--white); }

  .steps-tab { position: absolute; left: 0; top: 1079px; width: 235px; height: 29px; }
  .steps-title { position: absolute; left: 40px; top: 1081px; margin: 0; font-size: 23px; font-weight: 700; color: var(--white); }
  .steps-bar { position: absolute; left: 0; top: 1112px; width: 849px; height: 35px; background: var(--dark);
    display: flex; align-items: stretch; font-size: 24px; color: var(--white); }
  .step-letter { background: var(--orange); width: 24px; text-align: center; line-height: 35px; }
  .step-text { line-height: 35px; padding: 0 8px 0 10px; }
  .lead { width: 40px; }

  .footer { position: absolute; left: 0; top: 1162px; width: 100%; height: 38px; background: var(--dark); }
  .footer-line { position: absolute; left: 0; top: 1155px; width: 100%; height: 2px; background: var(--dark); }
  .footer-text { position: absolute; left: 43px; top: 1174px; margin: 0; font-size: 11px; color: var(--muted); }
</style>
</head>
<body>
<div class="flyer">
  <div class="top-band"></div>

  <h1 class="headline business-name">TUCK IT AT BRAMWOOD</h1>
  <p class="headline tagline">STORE IT DON’T SHIP IT</p>
  <p class="headline benefit benefit-less">FOR LESS</p>
  <p class="headline benefit benefit-convenience">CONVENIENCE</p>
  <p class="headline benefit benefit-quality">QUALITY</p>
  <p class="headline benefit benefit-service">SERVICE</p>

  <div class="box-illustration" role="img" aria-label="Two stacked cardboard boxes with a glowing light bulb on top and the hand-lettered slogan “LESS, is the new MORE” on the front box"></div>

  <table class="price-table">
    <tr><th>Box Size* (Approx)</th><th>Weight Limit</th><th>Price Per Month</th></tr>
    <tr><td>41 cm X 34 cm X 26 cm</td><td>10 Kilos</td><td>12 CHFs/per month</td></tr>
    <tr><td>48 cm X 43 cm X 35 cm</td><td>25 Kilos</td><td>25 CHFs/per month</td></tr>
  </table>
  <p class="footnote">* Larger sizes and prices available upon request.</p>

  <svg class="steps-tab" viewBox="0 0 235 29" aria-hidden="true">
    <polygon points="0,0 220,0 235,29 0,29" fill="var(--dark)"/>
  </svg>
  <h2 class="steps-title">Easy as ABC</h2>
  <div class="steps-bar">
    <span class="lead"></span>
    <span class="step-letter">A</span><span class="step-text">Contact us 064-293-5527</span>
    <span class="step-letter">B</span><span class="step-text">We deliver</span>
    <span class="step-letter">C</span><span class="step-text">We pick-up &amp; Store</span>
  </div>

  <div class="footer-line"></div>
  <div class="footer"></div>
  <p class="footer-text">For more information log onto www.tuckitbramwood.com</p>
</div>
</body>
</html>
```